Letterhead Design Project

Please see attached logo as well as information below which could be relevant to design. Let me know if you have any questions.

Derek J. Holloman
Estate Planning and Insurance Specialist
Dholloman@brenwickfinancial.com
P: 516-471-2958 F: 516-471-3085
www.brenwickfinancial.com
4300 Maple Ridge Road, Suite 305E
Fernhollow, New Ashby 11804

```html
<!DOCTYPE html>
<html lang="en">
<head>
<meta charset="utf-8">
<title>Brenwick Financial Group Letterhead</title>
<link rel="stylesheet" href="https://fonts.googleapis.com/css2?family=Arimo:wght@400;700&display=swap">
<style>
  :root {
    --navy: #2a2b38;
    --navy-deep: #1e1f2a;
    --gold: #c9b27c;
    --gold-light: #e3d3a6;
    --ink: #111111;
    --paper: #ffffff;
  }
  * { margin: 0; padding: 0; box-sizing: border-box; }
  html, body {
    width: 848px;
    height: 1200px;
    overflow: hidden;
    background: var(--paper);
  }
  .letterhead {
    position: relative;
    width: 848px;
    height: 1200px;
    background: var(--paper);
    font-family: "Arimo", Arial, sans-serif;
    color: var(--ink);
  }
  .header-band {
    position: absolute;
    top: 0;
    left: 0;
    width: 848px;
    height: 200px;
  }
  .brand {
    position: absolute;
    top: 19px;
    left: 74px;
    display: flex;
    align-items: center;
    gap: 16px;
  }
  .brand-square {
    width: 96px;
    height: 98px;
    border: 4px solid var(--gold);
  }
  .brand-name {
    font-weight: 700;
    font-size: 30px;
    letter-spacing: 1px;
    text-transform: uppercase;
    color: var(--gold-light);
    white-space: nowrap;
  }
  .footer {
    position: absolute;
    left: 0;
    top: 1073px;
    width: 848px;
  }
  .footer-rule-gold {
    position: absolute;
    left: 36px;
    top: 0;
    width: 777px;
    height: 4px;
    background: var(--gold);
  }
  .footer-rule-dark {
    position: absolute;
    left: 36px;
    top: 108px;
    width: 777px;
    height: 5px;
    background: var(--ink);
  }
  .contact-name {
    position: absolute;
    left: 27px;
    top: 16px;
    font-size: 14px;
    font-weight: 700;
    text-transform: uppercase;
  }
  .contact-row {
    position: absolute;
    left: 27px;
    width: 794px;
    display: flex;
    justify-content: space-between;
    font-size: 12px;
    font-weight: 700;
    text-transform: uppercase;
    letter-spacing: 0.1px;
    white-space: nowrap;
  }
  .row-title { top: 42px; }
  .row-address { top: 63px; }
  .row-phone { top: 84px; }
</style>
</head>
<body>
  <div class="letterhead">
    <svg class="header-band" viewBox="0 0 848 200" width="848" height="200" aria-hidden="true">
      <defs>
        <linearGradient id="bandFill" x1="0" y1="0" x2="0" y2="1">
          <stop offset="0" stop-color="#2f303e"/>
          <stop offset="1" stop-color="#22232f"/>
        </linearGradient>
        <filter id="bandShadow" x="-5%" y="-5%" width="110%" height="130%">
          <feDropShadow dx="0" dy="5" stdDeviation="5" flood-color="#000" flood-opacity="0.35"/>
        </filter>
      </defs>
      <path filter="url(#bandShadow)" fill="url(#bandFill)"
        d="M0 0 H848 V146 C790 140 720 134 640 140 C560 146 500 152 430 146 C340 138 260 130 180 140 C110 150 50 164 0 180 Z"/>
    </svg>

    <div class="brand">
      <div class="brand-square"></div>
      <div class="brand-name">Brenwick Financial Group</div>
    </div>

    <footer class="footer">
      <div class="footer-rule-gold"></div>
      <div class="contact-name">Derek J. Holloman</div>
      <div class="contact-row row-title">
        <span>Estate Planning and Insurance Specialist</span>
        <span>E-mail: Dholloman@brenwickfinancial.com</span>
      </div>
      <div class="contact-row row-address">
        <span>4300 Maple Ridge Road, Suite 305E Fernhollow, New Ashby 11804</span>
        <span>www.brenwickfinancial.com</span>
      </div>
      <div class="contact-row row-phone">
        <span>Phone : 555-471-2958 F: 555-471-3085</span>
      </div>
      <div class="footer-rule-dark"></div>
    </footer>
  </div>
</body>
</html>
```